Law Firm Website

We are a small California based law firm specializing in business, corporate and litigation matters. We need to have our website redesigned. We are looking for a new and fresh look for our site, keeping in mind that we are a law firm.
What we don't want:
**the traditional "gavel" and "scales of justice" look
**anything too crazy
What we do want:
**sophisticated yet modern and fresh corporate look and feel
**samples of websites we really like:
http://www.mtrhllp-example.com
http://www.orwenlatch-example.com/
we also like:
http://www.verdtolbain-example.com/
http://www.qh-example.com/
http://www.pembrost-example.com/
http://www.nvtr-example.com
http://www.rmqlaw-example.com/
The content will be whatever is currently on our website (www.halvencourtlaw-example.com). We will be selecting the winner based on originality and keeping the above requirements in mind. Please note that the photos that you use will be the ones that we will be using, so choose wisely because the photos will make a difference.
Target Market(s)
Corporate clients
Industry/Entity Type
Law Firm
Look and feel

```html
<!DOCTYPE html>
<html lang="en">
<head>
<meta charset="utf-8">
<title>Halvencourt Law Group, LLP</title>
<link href="https://fonts.googleapis.com/css2?family=Oswald:wght@300;400;500&family=Arimo:wght@400;700&display=swap" rel="stylesheet">
<style>
:root{
  --ink:#1f1f1f;
  --text:#333;
  --red:#b3221d;
  --red-dark:#8e1814;
  --blue:#1d77c9;
  --blue-dark:#0d5aa6;
  --bar:#2a2a2a;
  --rule:#d8d8d8;
  --band:#efefef;
  --white:#fff;
}
*{box-sizing:border-box;margin:0;padding:0}
html,body{width:1039px;height:1200px;overflow:hidden;background:var(--white)}
body{position:relative;font-family:"Arimo",Arial,sans-serif;color:var(--text);font-size:13px}
.abs{position:absolute}
.display{font-family:"Oswald","Arial Narrow",sans-serif}

/* header */
.brand-mark{left:36px;top:30px;width:64px;height:66px;background:linear-gradient(135deg,#5fb0ee,var(--blue-dark))}
.brand-name{left:114px;top:26px;font-family:"Oswald",sans-serif;font-weight:500;font-size:36px;color:var(--ink);letter-spacing:-.3px;white-space:nowrap}
.brand-tag{left:114px;top:76px;font-family:"Oswald",sans-serif;font-weight:500;font-size:15px;color:var(--ink);letter-spacing:.3px}
.nav a{position:absolute;top:74px;font-weight:700;font-size:12.5px;color:var(--ink);text-decoration:none;text-align:center;padding-bottom:6px;border-bottom:2px solid var(--ink);white-space:nowrap}
.nav a.current{color:var(--red);border-color:var(--red)}

/* hero */
.hero-photo{left:36px;top:125px;width:642px;height:288px;background:linear-gradient(90deg,#cfd6dc,#e9edf0 50%,#c9cfd3)}
.hero-stop{left:631px;top:384px;width:45px;height:26px;background:var(--white);border-radius:3px;font-size:11px;text-align:center;line-height:26px;color:var(--ink)}
.hero-panel{left:678px;top:125px;width:329px;height:288px;background:radial-gradient(circle at 75% 35%,#3a98e2,var(--blue) 45%,var(--blue-dark))}
.hero-copy{left:726px;top:201px;color:var(--white);font-family:"Oswald",sans-serif;text-transform:uppercase;line-height:1.25}
.hero-copy .small{font-weight:300;font-size:19px;letter-spacing:.3px}
.hero-copy .big{font-weight:500;font-size:31px;line-height:1.05;margin-top:6px}
.hero-cta{left:726px;top:316px;width:91px;height:31px;background:var(--red);border-radius:3px;color:var(--white);font-family:"Oswald",sans-serif;font-weight:500;font-size:14px;line-height:31px;text-align:center}
.hero-bar{left:36px;top:413px;width:971px;height:37px;background:var(--bar);color:var(--white)}
.hero-bar .clock{position:absolute;left:18px;top:11px;font-size:11.5px;display:flex;gap:8px;align-items:center}
.hero-bar .phone{position:absolute;right:22px;top:4px;font-family:"Oswald",sans-serif;font-size:20px;display:flex;gap:10px;align-items:center}

/* columns */
.col-title{top:490px;font-family:"Oswald",sans-serif;font-weight:400;font-size:22px;color:var(--ink)}
.col-img{top:548px;height:106px;border:1px solid #bbb}
.img-team{left:37px;width:300px;background:linear-gradient(90deg,#e6e6e6,#8a8f95 30%,#d9cfae 60%,#e5dcc2)}
.img-office{left:378px;width:300px;background:linear-gradient(180deg,#9a9a98,#c9b697 55%,#7c5a39)}
.reasons{left:36px;top:676px;list-style:none}
.reasons li{height:35.5px;padding-left:26px;position:relative;color:var(--red);font-size:13px}
.reasons li::before{content:"";position:absolute;left:2px;top:1px;width:13px;height:14px;background:var(--red);border-radius:2px;box-shadow:inset 0 0 0 3px var(--red),inset 0 0 0 5px #fff}
.about{left:380px;top:692px;width:296px;font-size:12.5px;line-height:19px;color:var(--text)}
.about p+p{margin-top:9px}
.about strong{color:var(--ink)}
.more-link{left:610px;top:853px;font-size:12.5px;color:var(--ink);text-decoration:underline}

.spot-arrows{left:968px;top:497px;display:flex;gap:3px}
.news-item{left:718px;width:290px}
.news-item .month{position:absolute;left:7px;top:0;font-weight:700;font-size:12px;color:var(--ink)}
.news-item .day{position:absolute;left:0;top:15px;width:39px;height:30px;background:var(--red);color:var(--white);border-radius:3px;text-align:center;font-size:15px;line-height:30px}
.news-item .date{position:absolute;left:49px;top:2px;font-size:12.5px;color:var(--ink);text-decoration:underline}
.news-item .title{position:absolute;left:49px;top:22px;font-weight:700;font-size:12.5px;color:var(--ink)}
.news-item .body{position:absolute;left:2px;top:48px;width:290px;font-size:12.5px;line-height:18px;word-break:break-all}
.btn-grey{position:absolute;left:2px;width:73px;height:23px;border:1px solid #c4c4c4;border-radius:3px;background:linear-gradient(#fff,#ddd);font-size:11.5px;text-align:center;line-height:21px;color:var(--ink)}

/* lower band */
.band{left:0;top:914px;width:1039px;height:204px;background:var(--band)}
.band-title{top:940px;font-family:"Oswald",sans-serif;font-size:19px;color:var(--red);display:flex;gap:6px;align-items:center;text-transform:uppercase}
.dots{top:978px;list-style:none}
.dots li{height:25px;padding-left:25px;position:relative;font-size:12.5px;color:var(--text)}
.dots li::before{content:"";position:absolute;left:2px;top:2px;width:11px;height:11px;border-radius:50%;background:var(--red);box-shadow:inset 0 0 0 3px #f6c9c6}
.newsletter{left:716px;top:934px;width:291px;height:134px;background:linear-gradient(135deg,#c8312a,#e0533f 55%,#b22a22);border:1px solid #a42019}
.newsletter h3{position:absolute;left:11px;top:10px;font-family:"Oswald",sans-serif;font-weight:400;font-size:24px;color:var(--white)}
.newsletter .note{position:absolute;left:12px;top:44px;font-size:10px;font-weight:700;color:#fbe0dc;text-transform:uppercase}
.newsletter .field{position:absolute;left:12px;top:64px;width:266px;height:21px;background:var(--white);border:1px solid #8b1a14}
.newsletter .send{position:absolute;right:13px;top:92px;width:82px;height:25px;background:linear-gradient(#fff,#ddd);border-radius:3px;font-weight:700;font-size:13px;text-align:center;line-height:25px;color:var(--ink)}

.footer{left:0;top:1118px;width:1039px;height:82px;border-top:3px solid #3a3a3a;background:linear-gradient(#cfcfcf,#f2f2f2 45%,#fff)}
.footer p{position:absolute;left:36px;top:37px;font-size:11px;color:var(--ink)}
</style>
</head>
<body>

<header>
  <div class="abs brand-mark"></div>
  <div class="abs brand-name">Halvencourt Law Group, LLP</div>
  <div class="abs brand-tag">NAME OF QUALITY LEGAL REPRESENTATION</div>
  <nav class="nav">
    <a class="current" style="left:532px;width:72px">HOME PAGE</a>
    <a style="left:630px;width:72px">ABOUT HLG</a>
    <a style="left:724px;width:105px">PRACTICE AREAS</a>
    <a style="left:857px;width:54px">LINKS</a>
    <a style="left:934px;width:72px">CONTACT</a>
  </nav>
</header>

<section class="hero">
  <div class="abs hero-photo" role="img" aria-label="Smiling senior attorney in front of colleagues in a bright office"></div>
  <div class="abs hero-stop">stop</div>
  <div class="abs hero-panel"></div>
  <div class="abs hero-copy">
    <div class="small">We do promise you fantastic</div>
    <div class="small">things, we just guarantee</div>
    <div class="big">Stability and<br>Progress</div>
  </div>
  <div class="abs hero-cta">CLICK HERE</div>
  <div class="abs hero-bar">
    <div class="clock">
      <svg width="12" height="12" viewBox="0 0 12 12"><circle cx="6" cy="6" r="5.5" fill="#fff"/><path d="M6 3v3h2.5" stroke="#2a2a2a" stroke-width="1.3" fill="none"/></svg>
      8.50 am, Thu March.13, 2014.
    </div>
    <div class="phone">
      <svg width="17" height="17" viewBox="0 0 17 17"><rect width="17" height="17" rx="2" fill="#fff"/><path d="M5 3.5l2 .5.5 2.5-1.2 1a6 6 0 003.2 3.2l1-1.2 2.5.5.5 2-1.5 1.5C8 13 4 9 3.5 5z" fill="#2a2a2a"/></svg>
      Phone: &nbsp;+1-555-014-2290
    </div>
  </div>
</section>

<main>
  <h2 class="abs col-title" style="left:36px">Why choose HLG?</h2>
  <div class="abs col-img img-team" role="img" aria-label="Attorney in glasses before a world map"></div>
  <ul class="abs reasons">
    <li>Lorem ipsum dolor sit ametmas massa astum</li>
    <li>Consectetuer adipi scing elit maurisumofnase</li>
    <li>demassa lorem estum dolore sedrumol sedo</li>
    <li>Aecenas hendrerit massa actumodesed acters</li>
    <li>Illa pulvinar nisl ac convallis seda massa lorem</li>
    <li>Tellus er sodales enim, in tincidut loerde dolore</li>
  </ul>

  <h2 class="abs col-title" style="left:378px">About the Firm</h2>
  <div class="abs col-img img-office" role="img" aria-label="Firm reception and lounge area"></div>
  <div class="abs about">
    <p><strong>Halvencourt Law Group, LLP</strong> takes pride in providing quality legal representation to its clients, whether they are large corporations, partnerships, or individuals.</p>
    <p>Our corporate clients benefit from the experience of our attorneys in the complex world of business, in addition to their keen legal skills. Our attorneys combine their thorough knowledge of the law with their personal experiences and...</p>
  </div>
  <a class="abs more-link">read more</a>

  <h2 class="abs col-title" style="left:719px">In The Spotlight</h2>
  <div class="abs spot-arrows">
    <svg width="18" height="18" viewBox="0 0 18 18"><circle cx="9" cy="9" r="9" fill="#aaa"/><path d="M4.5 11L9 6l4.5 5z" fill="#fff"/></svg>
    <svg width="18" height="18" viewBox="0 0 18 18"><circle cx="9" cy="9" r="9" fill="#aaa"/><path d="M4.5 7L9 12l4.5-5z" fill="#fff"/></svg>
  </div>
  <article class="abs news-item" style="top:544px">
    <span class="month">Feb</span><span class="day">30</span>
    <span class="date">30.02.2014</span>
    <span class="title">Doloremquedesaudantiindic totam</span>
    <p class="body">Werspiciatis unde omnis istnatus situm desasec voluptatem asdoloremquedesaudantiindic totam remi aperi eaque ipssivitaeco dicta sunt explica-booenimedelipsamvoluptateol quia sed massa</p>
    <span class="btn-grey" style="top:134px">Read more</span>
  </article>
  <article class="abs news-item" style="top:723px">
    <span class="month">Mar</span><span class="day">10</span>
    <span class="date">10.03.2014</span>
    <span class="title">Doloremquedesaudantiindic totam</span>
    <p class="body">Werspiciatis unde omnis istnatus situm desasec voluptatem asdoloremquedesaudantiindic totam remi aperi eaque ipssivitaeco dicta sunt exibition</p>
    <span class="btn-grey" style="top:115px">Read more</span>
  </article>
</main>

<section>
  <div class="abs band"></div>
  <h3 class="abs band-title" style="left:36px">
    <svg width="15" height="13" viewBox="0 0 15 13"><path d="M2 1h11a1 1 0 011 1v6a1 1 0 01-1 1H6l-3 3V9H2a1 1 0 01-1-1V2a1 1 0 011-1z" fill="none" stroke="#999" stroke-width="1.2"/></svg>
    Featured Services</h3>
  <ul class="abs dots" style="left:36px">
    <li>Lorem ipsum dolor sit ametmassame massa</li>
    <li>Consectetuer adipi scing elit mauriofi sedomi</li>
    <li>Aecenas hendrerit massa ac laosal duistemo</li>
    <li>Alla pulvinar nisl ac convallis nonuym seduma</li>
  </ul>
  <h3 class="abs band-title" style="left:378px">
    <svg width="15" height="13" viewBox="0 0 15 13"><path d="M2 1h11a1 1 0 011 1v6a1 1 0 01-1 1H6l-3 3V9H2a1 1 0 01-1-1V2a1 1 0 011-1z" fill="none" stroke="#999" stroke-width="1.2"/></svg>
    Time Management</h3>
  <ul class="abs dots" style="left:378px">
    <li>Lorem ipsum dolor sit ametmassame massa</li>
    <li>Consectetuer adipi scing elit mauriofi sedomi</li>
    <li>Aecenas hendrerit massa ac laosal duistemo</li>
    <li>Alla pulvinar nisl ac convallis nonuym seduma</li>
  </ul>
  <div class="abs newsletter">
    <h3>Newsletter</h3>
    <p class="note">Werspiciatis unde omnis istnatus situm</p>
    <div class="field"></div>
    <div class="send">subscribe</div>
  </div>
</section>

<footer class="abs footer">
  <p>Copyright © 2014 Halvencourt Law Group, LLP. All rights reserved.</p>
</footer>

</body>
</html>
```